BOLD & MINIMALIST DESIGN NEEDED

We want a very bold but minimalistic business card design that is impactful and utilizes both sides of the business card. Our current logo is included for your use.

We want bold fonts and good use of negative space. We don't want the logo to overpower the design.

Target Market(s)

Professionals who are building new commercial buildings.

Industry/Entity Type

Construction

Contact Information for Business Card

Name, Title, email, office phone, cell phone, website

Font styles to use
Serif
Sans Serif

Requirements
Must have
• Bold design!

```html
<!DOCTYPE html>
<html lang="en">
<head>
<meta charset="utf-8">
<title>Ridgeline Business Card</title>
<link rel="stylesheet" href="https://fonts.googleapis.com/css2?family=Montserrat:wght@800&family=Fira+Sans:wght@400&display=swap">
<style>
  :root {
    --stage: #1d1e1f;
    --lime: #86c22a;
    --ink: #0b0b0c;
    --paper: #ffffff;
    --soft: #e8e8e8;
  }
  * { box-sizing: border-box; margin: 0; padding: 0; }
  html, body { width: 1200px; height: 1122px; overflow: hidden; }
  body { background: var(--stage); position: relative; font-family: "Fira Sans", sans-serif; }

  .card {
    position: absolute;
    left: 170px;
    width: 860px;
    height: 492px;
    border-radius: 28px;
    overflow: hidden;
  }
  .card--back { top: 49px; background: var(--lime); }
  .card--front { top: 581px; background: var(--paper); }

  .brand {
    position: absolute;
    display: flex;
    align-items: center;
    gap: 18px;
    font-family: "Montserrat", sans-serif;
    font-weight: 800;
    color: var(--ink);
    letter-spacing: 1px;
  }
  .card--back .brand { left: 50%; top: 50%; transform: translate(-50%, -50%); font-size: 72px; }
  .brand__square { width: 40px; height: 40px; background: var(--ink); }

  .card--front .brand { left: 50%; top: 88px; transform: translateX(-50%); font-size: 72px; }

  .front-band { position: absolute; inset: 0; width: 860px; height: 492px; }

  .person {
    position: absolute;
    right: 480px;
    top: 300px;
    text-align: right;
  }
  .person__name {
    font-family: "Montserrat", sans-serif;
    font-weight: 800;
    font-size: 34px;
    color: var(--lime);
    letter-spacing: 0.5px;
  }
  .person__title { font-size: 20px; color: var(--soft); margin-top: 4px; }

  .divider {
    position: absolute;
    left: 410px;
    top: 298px;
    width: 2px;
    height: 130px;
    background: var(--lime);
  }

  .contacts {
    position: absolute;
    left: 432px;
    top: 306px;
    list-style: none;
  }
  .contacts li {
    display: flex;
    align-items: center;
    gap: 12px;
    height: 31px;
    font-size: 19px;
    color: var(--soft);
  }
  .contacts svg { width: 16px; height: 16px; flex: none; }
</style>
</head>
<body>

<section class="card card--back">
  <div class="brand"><span class="brand__square"></span>RIDGELINE</div>
</section>

<section class="card card--front">
  <svg class="front-band" viewBox="0 0 860 492" aria-hidden="true">
    <path d="M0 200 C 320 150, 640 230, 860 492 L 0 492 Z" fill="#0b0b0c"/>
  </svg>

  <div class="brand">RIDGELINE</div>

  <div class="person">
    <p class="person__name">MARCUS HALE</p>
    <p class="person__title">Founder &amp; CEO</p>
  </div>

  <span class="divider"></span>

  <ul class="contacts">
    <li>
      <svg viewBox="0 0 16 16"><path d="M3 1h3l1.5 4-2 1.3a9 9 0 0 0 4.2 4.2L11 8.5l4 1.5v3a2 2 0 0 1-2 2A12 12 0 0 1 1 3a2 2 0 0 1 2-2z" fill="#86c22a"/></svg>
      (555) 014-2290
    </li>
    <li>
      <svg viewBox="0 0 16 16"><rect x="4" y="1" width="8" height="14" rx="1.5" fill="none" stroke="#86c22a" stroke-width="1.6"/><circle cx="8" cy="12.5" r="0.9" fill="#86c22a"/></svg>
      (555) 014-2291
    </li>
    <li>
      <svg viewBox="0 0 16 16"><rect x="1" y="3" width="14" height="10" fill="#86c22a"/><path d="M1 3l7 6 7-6" fill="none" stroke="#0b0b0c" stroke-width="1.3"/></svg>
      info@ridgelinebuild.com
    </li>
    <li>
      <svg viewBox="0 0 16 16"><circle cx="8" cy="8" r="6.5" fill="none" stroke="#86c22a" stroke-width="1.6"/><path d="M1.5 8h13M8 1.5c-3 3.5-3 9.5 0 13M8 1.5c3 3.5 3 9.5 0 13" fill="none" stroke="#86c22a" stroke-width="1.2"/></svg>
      ridgelinebuild.com
    </li>
  </ul>
</section>

</body>
</html>
```